I need a business card designed using the logo provided either vertical or horizontal......Tallowmere Advisory is an Australian based real estate company that caters for the upper end of the market so the design of the business card "must reflect" the companies image!!
Colour combinations are optional but "must be realistic" and must be able to be accurately useable CMYK colours.
Please consider that any colours used "must be able to be used" and be suitable in following designs for "pull out banner signs" and "real estate signs".
The colours and the font in the attached designs are for example and other combinations are encouraged.
Target Market(s)
The High End of the Australian real estate market
Industry/Entity Type
Business
Contact Information for Business Card
Logo - Business Name - Director + Licensed Real Estate Agent - Mobile Number (Cell Phone) - Business Number - Fax - Email Address - Web address
Requirements
Must have
- Designs and colours (CMYK) that can easily be interpreted by an Australian printer.
Nice to have
- Some alternative ideas on colour and font..........the ones provided are ok and have been provided as an example but I am looking for alternative ideas
Should not have
- Loud, overly bright colours. Designs that do not reflect the professional standards of the business.
- Designs that look good on a computer monitor but can not be re-created on a printing press.............this is most important when it comes to shading etc.

```html
<!DOCTYPE html>
<html lang="en">
<head>
<meta charset="utf-8">
<title>Tallowmere Advisory – Business Card</title>
<link rel="stylesheet" href="https://fonts.googleapis.com/css2?family=Michroma&family=Roboto+Condensed:wght@400;700&display=swap">
<style>
  :root {
    --backdrop: #e9e7e3;
    --card: #fbfbfa;
    --gold: #c9a430;
    --gold-deep: #b48f1f;
    --gold-light: #d9b944;
    --ink: #2b2b2b;
    --ink-soft: #3a3a3a;
    --white: #ffffff;
  }
  * { margin: 0; padding: 0; box-sizing: border-box; }
  html, body {
    width: 1200px; height: 892px; overflow: hidden;
    background: var(--backdrop);
  }
  .canvas {
    width: 1200px; height: 892px;
    display: flex; align-items: center; justify-content: center;
  }
  .card {
    position: relative;
    width: 1000px; height: 570px;
    background: linear-gradient(135deg, var(--white) 0%, var(--card) 60%, #f1f1ef 100%);
    box-shadow: 0 12px 30px rgba(0,0,0,0.18);
    overflow: hidden;
  }
  .band {
    position: absolute; left: 0; top: 0; bottom: 0; width: 236px;
    background: linear-gradient(180deg, var(--gold-light) 0%, var(--gold) 55%, var(--gold-deep) 100%);
  }
  .band-stripe {
    position: absolute; top: 0; bottom: 0; width: 5px; background: var(--white);
  }
  .band-stripe--inner { left: 208px; }
  .band-rule {
    position: absolute; top: 0; bottom: 0; left: 246px; width: 4px; background: var(--gold);
  }
  .band-notch {
    position: absolute; left: 236px; width: 10px; height: 8px; background: var(--gold);
  }
  .band-notch--one { bottom: 22px; }
  .band-notch--two { bottom: 6px; }
  .brand-mark {
    position: absolute; left: 58px; top: 150px; width: 150px; height: 150px;
    border-radius: 50%; border: 4px solid rgba(255,255,255,0.75);
  }
  .content {
    position: absolute; left: 290px; top: 70px; right: 40px;
  }
  .brand-name {
    font-family: "Michroma", sans-serif;
    font-weight: 400;
    color: var(--ink);
    font-size: 54px;
    line-height: 1.1;
    letter-spacing: 1px;
    text-transform: uppercase;
  }
  .person { margin-top: 52px; }
  .person-name {
    font-family: "Roboto Condensed", sans-serif;
    font-weight: 700; font-size: 44px; color: var(--gold);
    line-height: 1;
  }
  .person-title {
    font-family: "Roboto Condensed", sans-serif;
    font-size: 19px; color: var(--ink-soft); margin-top: 6px;
  }
  .contacts { list-style: none; margin-top: 34px; }
  .contact {
    display: flex; align-items: center; gap: 16px;
    font-family: "Roboto Condensed", sans-serif;
    font-size: 27px; color: var(--ink); line-height: 1.22;
  }
  .contact-key {
    width: 20px; height: 20px; background: var(--gold);
    color: var(--white); font-size: 12px; font-weight: 700;
    display: flex; align-items: center; justify-content: center;
    flex: none;
  }
</style>
</head>
<body>
<main class="canvas">
  <section class="card" aria-label="Tallowmere Advisory business card">
    <div class="band">
      <span class="band-stripe band-stripe--inner"></span>
      <span class="brand-mark" aria-hidden="true"></span>
    </div>
    <span class="band-rule"></span>
    <span class="band-notch band-notch--one"></span>
    <span class="band-notch band-notch--two"></span>

    <div class="content">
      <h1 class="brand-name">Tallowmere<br>Advisory</h1>

      <div class="person">
        <p class="person-name">Employee name</p>
        <p class="person-title">Managing Director</p>
      </div>

      <ul class="contacts">
        <li class="contact"><span class="contact-key">P</span>02 9410 3827</li>
        <li class="contact"><span class="contact-key">W</span>www.tallowmere.com.au</li>
        <li class="contact"><span class="contact-key">E</span>hello@tallowmere.com.au</li>
        <li class="contact"><span class="contact-key">A</span>Level 4, 18 Harbourview Tce Sydney NSW 2000</li>
      </ul>
    </div>
  </section>
</main>
</body>
</html>
```